Designs for a fundrasining event a Brown Tie Beer and Wine event

We need a flyer, brochure, and tickets for entry for a brown tie event that will be a beer and wine pairing fundraising event to be held on May 9th from 6pm to 10pm at the harborview Bistro in Cedar Lake, Indiana, USA. There will be approximately 10 silent auction items and 5 or so sponsors that we will want to have the logos of the sponsors on what we can as well, attached are the logo for Hand in Hand Foundation, IV NFP, which is the nonprofit hosting the event, there is also a logo for Mosley Counsel, LLC which is one of the sponsors (this is so you have an idea of the other 4 or so that we would also want incorporated somehow). Please ask as many questions as you may have to clarify.

Industry/Entity Type

Event

Contact Information for Business Card

Hand in Hand
Nora T. Whitfield
President/CEO
(555)382-9046
www.handinhandfdn.example

New Card:
Peter J. Whitfield
Director
(555)309-6254
www.handinhandfdn.example

New Card:
Alice M. Whitfield
Director
www.handinhandfdn.example

New Card:
Gregory B. Whitfield
Director
www.handinhandfdn.example

Font styles to use
Script

Requirements
Must have
• I want a clean card for all 4 individuals with the logo that was attached.

```html
<!DOCTYPE html>
<html lang="en">
<head>
<meta charset="utf-8">
<title>Wine and Beer Tasting – Admission Ticket</title>
<link rel="stylesheet" href="https://fonts.googleapis.com/css2?family=Arimo&family=Josefin+Sans:wght@400&family=Parisienne&display=swap">
<style>
  :root {
    --leaf-light: #dbe9a8;
    --leaf: #c8dc84;
    --leaf-deep: #b9d06e;
    --ink: #111111;
    --wine-red: #a63128;
    --amber: #c7782f;
    --amber-light: #d9973f;
    --cream: #f2efdc;
    --oval: #ecebdc;
    --glass-red: #7a1616;
    --glass-gold: #e8b530;
  }
  * { margin: 0; padding: 0; box-sizing: border-box; }
  html, body { width: 1200px; height: 686px; overflow: hidden; background: #ffffff; }
  .ticket {
    position: relative;
    width: 1200px;
    height: 686px;
    overflow: hidden;
    background: linear-gradient(115deg, var(--leaf-deep) 0%, var(--leaf) 45%, var(--leaf-light) 100%);
    color: var(--ink);
    font-family: "Josefin Sans", sans-serif;
  }
  .flourish {
    position: absolute;
    top: 62px;
    height: 30px;
    border-radius: 15px;
    background: linear-gradient(90deg, rgba(242,239,220,0.35), rgba(242,239,220,0.85), rgba(242,239,220,0.35));
  }
  .flourish--left { left: 82px; width: 330px; }
  .flourish--right { left: 714px; width: 292px; }
  .admit {
    position: absolute;
    top: 56px;
    left: 412px;
    width: 302px;
    text-align: center;
    font-family: "Arimo", sans-serif;
    font-size: 36px;
    letter-spacing: 1px;
  }
  .title {
    position: absolute;
    top: 110px;
    left: 40px;
    width: 1000px;
    text-align: center;
    font-family: "Parisienne", cursive;
    font-size: 118px;
    line-height: 1.2;
    white-space: nowrap;
  }
  .title__wine, .title__tasting { color: var(--wine-red); }
  .title__and { color: var(--cream); }
  .title__beer { color: var(--amber); }
  .details {
    position: absolute;
    top: 268px;
    left: 290px;
    width: 700px;
    text-align: center;
  }
  .details__line { font-size: 54px; line-height: 75px; height: 75px; }
  .details__venue { font-size: 38px; font-variant: small-caps; font-size: 46px; letter-spacing: 1px; }
  .auction {
    position: absolute;
    left: 9px;
    top: 286px;
    width: 334px;
    height: 257px;
    border-radius: 50%;
    background: var(--oval);
    box-shadow: inset 0 14px 18px rgba(90,100,60,0.35);
    display: flex;
    flex-direction: column;
    align-items: center;
    justify-content: center;
    font-family: "Parisienne", cursive;
    color: var(--wine-red);
    font-size: 56px;
    line-height: 64px;
    padding-top: 6px;
  }
  .glasses {
    position: absolute;
    left: 980px;
    top: 18px;
    width: 220px;
    height: 656px;
    border-radius: 60px 0 30px 30px;
    background: linear-gradient(180deg, var(--glass-red) 0%, var(--glass-red) 38%, var(--glass-gold) 55%, var(--amber-light) 100%);
    opacity: 0.9;
  }
</style>
</head>
<body>
  <main class="ticket">
    <div class="flourish flourish--left" role="img" aria-label="Decorative scroll ornament"></div>
    <p class="admit">ADMIT ONE</p>
    <div class="flourish flourish--right" role="img" aria-label="Decorative scroll ornament"></div>

    <h1 class="title">
      <span class="title__wine">Wine</span>
      <span class="title__and">and</span>
      <span class="title__beer">Beer</span>
      <span class="title__tasting">Tasting</span>
    </h1>

    <div class="auction">
      <span>Silent auction</span>
      <span>7-9 pm</span>
    </div>

    <section class="details">
      <p class="details__line">Saturday, May 9, 2015</p>
      <p class="details__line">6 pm to10 pm</p>
      <p class="details__line details__venue">Harborview Bistro</p>
      <p class="details__line">4280 Meridian Ave.</p>
      <p class="details__line">Cedar Lake, IN</p>
    </section>

    <div class="glasses" role="img" aria-label="Illustration of a glass of red wine leaning on a tall glass of beer"></div>
  </main>
</body>
</html>
```